Stationary - Business Card/Letterhead and envelope design

Details for my new Stationery Design Project will be added soon. , I have two logos I am trying to decide on. I will upload the eps logos shortly. I have attached a file of what i have so far. I need urgently Business cards, but also will need a letterhead template and envelopes.

PLEASE NOTE THE DEADLINE SAYS 2 DAYS but I need business card design in LESS THAN A DAY.

thanks, Details for my new Stationery Design Project will be added soon. , I have two logos I am trying to decide on. I will upload the eps logos shortly. I have attached a file of what i have so far. I need urgently Business cards, but also will need a letterhead template and envelopes.

thanks
Updates

I have uploaded one of the logos you can work with. hopefully the other one comes soon.

details for the business card.

Marla Thorne

Managing Director

P&K Ventures Ltd

Bda: 1-441-555-0193

Email: marla@pkvnbda.com

web: www.pkvnbda.com

Industry/Entity Type

Business

```html
<!DOCTYPE html>
<html lang="en">
<head>
<meta charset="utf-8">
<title>P&amp;K Ventures Ltd — Envelope</title>
<link href="https://fonts.googleapis.com/css2?family=Montserrat:wght@400;600&display=swap" rel="stylesheet">
<style>
  :root {
    --backdrop: #e4e4e4;
    --paper: #f7f7f7;
    --teal: #2b9aac;
    --brown: #7f6a56;
    --ink: #8a7866;
  }
  * { margin: 0; padding: 0; box-sizing: border-box; }
  html, body {
    width: 1200px; height: 900px; overflow: hidden;
    background: var(--backdrop);
    font-family: "Montserrat", Arial, sans-serif;
  }
  .canvas { position: relative; width: 1200px; height: 900px; }

  .envelope {
    position: absolute; left: 180px; width: 840px; height: 400px;
    background: var(--paper);
    box-shadow: 0 4px 14px rgba(0,0,0,0.12);
    overflow: hidden;
  }
  .envelope--front { top: 40px; }
  .envelope--back { top: 470px; }

  .brand-name {
    position: absolute; left: 44px; top: 38px;
    font-size: 30px; font-weight: 600; letter-spacing: 0.5px;
    color: var(--teal);
  }
  .return-address {
    position: absolute; left: 44px; top: 150px;
    font-size: 14px; line-height: 1.5; color: var(--ink);
  }
  .band { position: absolute; }
  .band--teal { left: 0; top: 300px; width: 210px; height: 22px; background: var(--teal); }
  .band--brown { left: 210px; top: 322px; width: 630px; height: 22px; background: var(--brown); }

  .contact {
    position: absolute; top: 262px;
    font-size: 13px; line-height: 1.6; color: var(--ink);
    list-style: none;
  }
  .contact--phones { left: 256px; }
  .contact--online { left: 410px; }
  .contact li { display: flex; align-items: center; gap: 6px; }
  .contact svg { width: 11px; height: 11px; fill: var(--teal); flex: none; }

  .flap {
    position: absolute; left: 0; top: 0; width: 840px; height: 110px;
    background: var(--teal);
    border-bottom-right-radius: 28px;
  }
</style>
</head>
<body>
<main class="canvas">
  <section class="envelope envelope--front" aria-label="Envelope front">
    <div class="brand-name">P&amp;K Ventures Ltd</div>
    <address class="return-address" style="font-style:normal">
      18 Harbour Lane<br>Hamilton, Bermuda HM 11
    </address>

    <ul class="contact contact--phones">
      <li>
        <svg viewBox="0 0 12 12" aria-hidden="true"><path d="M2.5 1h2l1 3-1.3 1a6.5 6.5 0 0 0 2.8 2.8L8 6.5l3 1v2A1.5 1.5 0 0 1 9.5 11 8.5 8.5 0 0 1 1 2.5 1.5 1.5 0 0 1 2.5 1z"/></svg>
        1-441-555-0193
      </li>
      <li>
        <svg viewBox="0 0 12 12" aria-hidden="true"><path d="M3.5 0h5A1 1 0 0 1 9.5 1v10a1 1 0 0 1-1 1h-5a1 1 0 0 1-1-1V1a1 1 0 0 1 1-1zm.5 1.5v8h4v-8z"/></svg>
        1-441-555-0148
      </li>
    </ul>
    <ul class="contact contact--online">
      <li>
        <svg viewBox="0 0 12 12" aria-hidden="true"><path d="M0 2h12v8H0zm1 1v.4l5 3.2 5-3.2V3z"/></svg>
        marla@pkvnbda.com
      </li>
      <li>
        <svg viewBox="0 0 12 12" aria-hidden="true"><circle cx="6" cy="6" r="5.5"/></svg>
        www.pkvnbda.com
      </li>
    </ul>

    <div class="band band--teal"></div>
    <div class="band band--brown"></div>
  </section>

  <section class="envelope envelope--back" aria-label="Envelope back">
    <div class="flap"></div>
  </section>
</main>
</body>
</html>
```